A hand soap seller needs a premium label for a new product

We need a premium label for a bottle of soap. We want to write on it:
VANTROSELLA (Name)
Hypoallergenic and antibacterial hand soap
350 ml e / 11.8 fl oz (volume, http://pimaxo.ru/7K3RtWbqmeL519)
Saint Petersburg - Russia / www.vantrosella.ru
We want to see the face of a hippopotamus in the design. Use only black and white and green for accents (the color of grass). Examples of a hippopotamus are shown in the photo. Our soap is hypoallergenic. Ideal for both children and adults. Therefore, the label should appeal to adults and children.
The bottle will be white, and the soap dispenser will be black.
So I'm attaching an example of a soap design that we liked
Label size: height-78 mm, width-102 mm !!!

Target Market(s)

Mothers and children

Industry/Entity Type

Hand soap

Font styles to use
Serif

Colors

Designer to choose only greyscale colors for use in the design.

Requirements
Must have
• The face of a hippopotamus emerging from the grass, Black and white palette with elements of green (grass color)
Nice to have
• The face of a hippopotamus emerging from the grass
Should not have
• Different colors

```html
<!DOCTYPE html>
<html lang="en">
<head>
<meta charset="utf-8">
<title>Vantrosella — Hypoallergenic Hand Soap Label</title>
<link rel="stylesheet" href="https://fonts.googleapis.com/css2?family=Montserrat:wght@400;500;700&family=Open+Sans+Condensed:wght@300&display=swap">
<style>
  :root {
    --page-bg: #f2f2f2;
    --label-bg: #ffffff;
    --label-edge: #e4e4e4;
    --ink: #1d1d1f;
    --ink-soft: #9a9a9a;
    --grass: #8fbf1f;
    --lime: #d2d400;
    --hippo-grey: #c6c7ca;
  }
  * { margin: 0; padding: 0; box-sizing: border-box; }
  html, body {
    width: 1109px;
    height: 1200px;
    overflow: hidden;
    background: var(--page-bg);
  }
  .canvas {
    position: relative;
    width: 1109px;
    height: 1200px;
  }
  .label {
    position: absolute;
    left: 54px;
    top: 217px;
    width: 1000px;
    height: 765px;
    background: var(--label-bg);
    border: 1px solid var(--label-edge);
    box-shadow: 0 6px 24px rgba(0,0,0,0.06);
    font-family: "Montserrat", sans-serif;
    color: var(--ink);
  }
  .brand-name {
    position: absolute;
    left: 205px;
    top: 44px;
    font-size: 116px;
    font-weight: 400;
    letter-spacing: 1px;
    line-height: 1;
  }
  .product-line {
    position: absolute;
    left: 214px;
    top: 189px;
    height: 88px;
    padding-left: 22px;
    border-left: 8px solid var(--grass);
    display: flex;
    flex-direction: column;
    justify-content: center;
    gap: 6px;
  }
  .product-line .claim {
    font-size: 35px;
    font-weight: 500;
    letter-spacing: 0.5px;
    line-height: 1;
  }
  .product-line .product {
    font-size: 42px;
    font-weight: 700;
    letter-spacing: 0.5px;
    line-height: 1;
  }
  .character-art {
    position: absolute;
    left: 184px;
    top: 311px;
    width: 565px;
    height: 384px;
  }
  .origin-note {
    position: absolute;
    left: 952px;
    top: 203px;
    height: 432px;
    writing-mode: vertical-rl;
    transform: rotate(180deg);
    font-family: "Open Sans Condensed", sans-serif;
    font-weight: 300;
    font-size: 21px;
    color: var(--ink-soft);
    white-space: nowrap;
    text-align: center;
  }
  .volume {
    position: absolute;
    right: 22px;
    top: 710px;
    font-family: "Open Sans Condensed", sans-serif;
    font-weight: 300;
    font-size: 25px;
    color: var(--ink-soft);
  }
</style>
</head>
<body>
  <main class="canvas">
    <section class="label">
      <h1 class="brand-name">Vantrosella</h1>

      <div class="product-line">
        <span class="claim">HYPOALLERGENIC</span>
        <span class="product">HAND SOAP</span>
      </div>

      <svg class="character-art" viewBox="0 0 565 384" role="img" aria-label="Illustration of a friendly grey hippopotamus standing among green and lime blobs and grass strokes">
        <defs>
          <radialGradient id="artTone" cx="50%" cy="50%" r="60%">
            <stop offset="0%" stop-color="var(--hippo-grey)"/>
            <stop offset="55%" stop-color="#d8dbc4"/>
            <stop offset="100%" stop-color="#e9efc9"/>
          </radialGradient>
        </defs>
        <rect x="0" y="0" width="565" height="384" rx="40" fill="url(#artTone)"/>
      </svg>

      <p class="origin-note">Saint Petersburg - Russia / www.vantrosella.ru</p>

      <p class="volume">350 ml e / 11.8 fl oz</p>
    </section>
  </main>
</body>
</html>
```